Crestwell Advisory Services

I'm looking to create a flyer for my business to provide a consultant service. I will be providing the following below
Launch Your Business Today for only $150
(state fee not included)
Business Formation includes:
*Limited liability Corporation (LLC)
*Halvers and Quint Number
*FEIN
*Operation Agreement for partnership LLCs (For 2 or more member(s)
*Commercial Activity license (If needed for your Business )
*Same -day turnaround service with documents
Schedule your Appointment today
Call or text:318-472-6051
Email:MoralesCapitalCircle@fernmail.net
Target Market(s)
I want the flyer to attract people who wants to start a business but doesn’t know where to start. I want the flyer to stand out form the other consultant businesses.
Industry/Entity Type
Consultant
Requirements
Must have
- The State fee not included should be in small print
Highlight the price or service
Highlight the phrase "launch you business today"
Nice to have
- Different samples of colors, a variety
Should not have
- should not be all one color

```html
<!DOCTYPE html>
<html lang="en">
<head>
<meta charset="utf-8">
<title>Launch Your Business Today</title>
<link rel="stylesheet" href="https://fonts.googleapis.com/css2?family=League+Spartan:wght@400;600;700&family=Mulish:wght@300;400&display=swap">
<style>
  :root {
    --stage: #939499;
    --ink: #21232b;
    --teal: #41a48c;
    --teal-panel: rgba(67, 160, 138, 0.92);
    --orange: #e67a3b;
    --orange-panel: #e98c4f;
    --gold: #f6a93b;
    --slate: #4a4b50;
    --icon-blue: #5b7fc0;
    --phone-blue: #7094d6;
    --rule-copper: #b8683a;
    --white: #ffffff;
  }
  * { box-sizing: border-box; margin: 0; padding: 0; }
  html, body {
    width: 896px; height: 1200px; overflow: hidden;
    background: var(--stage);
  }
  .flyer {
    position: absolute; left: 78px; top: 76px;
    width: 737px; height: 1041px;
    background: var(--ink);
    overflow: hidden;
    font-family: "Mulish", sans-serif;
    color: var(--white);
  }
  .flyer > * { position: absolute; }

  .brand { left: 39px; top: 48px; color: var(--teal); font-family: "League Spartan", sans-serif; font-weight: 700; white-space: nowrap; }
  .brand-name { font-size: 40px; line-height: 1; letter-spacing: 0.5px; }
  .brand-tag { font-size: 13px; letter-spacing: 5.4px; margin-top: 6px; padding-left: 3px; }

  .social { left: 546px; top: 78px; display: flex; gap: 6px; }
  .social span { width: 25px; height: 25px; border-radius: 50%; background: var(--icon-blue); display: block; }

  .photo {
    left: 0; top: 148px; width: 737px; height: 701px;
    background:
      radial-gradient(ellipse at 18% 25%, rgba(255,246,236,0.95) 0%, rgba(240,224,210,0.6) 35%, rgba(0,0,0,0) 60%),
      linear-gradient(100deg, #eadfd6 0%, #c8b3a6 30%, #7d6a6a 48%, #33395a 68%, #1d2444 85%, #141a30 100%);
  }

  .headline { left: 0; top: 0; width: 737px; font-family: "League Spartan", sans-serif; }
  .headline span { position: absolute; white-space: nowrap; line-height: 1; }
  .headline-lead { left: 84px; top: 176px; font-size: 44px; font-weight: 400; color: var(--slate); letter-spacing: -1px; }
  .headline-main { left: 44px; top: 219px; font-size: 102px; font-weight: 700; color: var(--orange); letter-spacing: -1px; }
  .headline-sub { left: 59px; top: 303px; font-size: 86px; font-weight: 700; color: var(--teal); letter-spacing: -1px; }

  .price-card {
    left: 75px; top: 408px; width: 237px; height: 199px;
    background: var(--orange-panel);
    border-top-left-radius: 26px;
    text-align: center;
  }
  .price-label { margin-top: 24px; font-family: "League Spartan", sans-serif; font-weight: 700; font-size: 17px; letter-spacing: 4px; color: var(--ink); padding-left: 4px; }
  .price-amount { font-family: "League Spartan", sans-serif; font-weight: 700; color: var(--white); line-height: 1; margin-top: 4px; white-space: nowrap; }
  .price-amount .currency { font-size: 46px; vertical-align: 36px; margin-right: 2px; }
  .price-amount .figure { font-size: 100px; letter-spacing: -3px; }
  .price-note { font-size: 16px; font-weight: 300; color: var(--ink); margin-top: 0; white-space: nowrap; }

  .includes {
    left: 75px; top: 628px; width: 237px; height: 381px;
    background: var(--teal-panel);
    border-bottom-right-radius: 40px;
    padding: 20px 14px 0 21px;
  }
  .includes-title { font-family: "League Spartan", sans-serif; font-weight: 700; font-size: 34px; line-height: 0.94; color: var(--gold); white-space: nowrap; }
  .includes-rule { height: 2px; background: var(--gold); margin: 9px 6px 12px 0; }
  .includes-list { list-style: none; font-size: 13px; font-weight: 400; line-height: 1.17; }
  .includes-list li { position: relative; padding-left: 12px; margin-bottom: 8px; }
  .includes-list li::before { content: ""; position: absolute; left: 0; top: 5px; width: 4px; height: 4px; border-radius: 50%; background: var(--white); }

  .appointment {
    left: 335px; top: 892px; width: 331px; height: 62px;
    border: 1px solid var(--rule-copper);
    border-top-right-radius: 20px;
    padding: 10px 0 0 14px;
    font-family: "League Spartan", sans-serif; font-weight: 700;
    font-size: 23px; line-height: 1.0; letter-spacing: 1.8px; color: var(--teal);
    white-space: nowrap;
  }
  .contact { left: 350px; top: 962px; font-size: 15.5px; line-height: 1.25; white-space: nowrap; }
  .contact .phone { font-family: "League Spartan", sans-serif; font-weight: 700; font-size: 23px; color: var(--phone-blue); letter-spacing: 0.5px; }
</style>
</head>
<body>
  <main class="flyer">
    <header class="brand">
      <div class="brand-name">CRESTWELL</div>
      <div class="brand-tag">ADVISORY SERVICES</div>
    </header>
    <div class="social" aria-hidden="true"><span></span><span></span><span></span><span></span></div>

    <div class="photo" role="img" aria-label="Photo of two businessmen in suits smiling while reviewing documents on a tablet in a bright office"></div>

    <h1 class="headline">
      <span class="headline-lead">Launch Your</span>
      <span class="headline-main">BUSINESS</span>
      <span class="headline-sub">TODAY</span>
    </h1>

    <section class="price-card">
      <p class="price-label">FOR ONLY</p>
      <p class="price-amount"><span class="currency">$</span><span class="figure">150</span></p>
      <p class="price-note">(state fee not included)</p>
    </section>

    <section class="includes">
      <h2 class="includes-title">BUSINESS<br>FORMATION<br>INCLUDES:</h2>
      <div class="includes-rule"></div>
      <ul class="includes-list">
        <li>Limited liability Corporation (LLC)</li>
        <li>Halvers and Quint Number</li>
        <li>FEIN</li>
        <li>Operation Agreement for partnership LLCs<br>(For 2 or more member(s)</li>
        <li>Commercial Activity license<br>(If needed for your Business )</li>
        <li>Same -day turnaround service with documents</li>
      </ul>
    </section>

    <h2 class="appointment">SCHEDULE YOUR<br>APPOINTMENT TODAY</h2>
    <p class="contact">
      Call or Text: <span class="phone">318-472-6051</span><br>
      Email: MoralesCapitalCircle@fernmail.net
    </p>
  </main>
</body>
</html>
```